Let Us Bloom speaking engagement

the flyer is about a speaking engagement for women's groups. Flyer should be simple, soft, engaging, clean and professional. I am a life coach and also a talk show host. the event I will be advertising is for groups of women. It will be given to church groups, female clubs and organizations. The name of my company is Mara's Lantern Life Coaching Institute.

Target Market(s)

professional women over thirty years old

Font styles to use
Script

Colors
ffffff
34a7d8
85cae6

Requirements
Must have
• use my photo and logo only
Should not have
• anything distracting

```html
<!DOCTYPE html>
<html lang="en">
<head>
<meta charset="utf-8">
<title>Let Us Bloom – Speaking Engagement Flyer</title>
<link href="https://fonts.googleapis.com/css2?family=Anton&family=Archivo+Black&family=Lato:wght@400;700&display=swap" rel="stylesheet">
<style>
  :root {
    --page-bg: #e9ecef;
    --paper: #ffffff;
    --ink: #1f1f1f;
    --body-ink: #555b60;
    --blue-strong: #34a7d8;
    --blue-deep: #2f86c4;
    --blue-soft: #85cae6;
    --blue-mist: #cfe7f4;
    --line-dark: #3a3a3a;
    --photo-top: #d9d4c4;
    --photo-mid: #6f6a78;
    --photo-low: #2f3f8a;
  }
  * { margin: 0; padding: 0; box-sizing: border-box; }
  html, body {
    width: 1200px; height: 984px; overflow: hidden;
    background: var(--page-bg);
  }
  .flyer {
    position: absolute; left: 250px; top: 36px;
    width: 700px; height: 912px;
    background: var(--paper);
    overflow: hidden;
    box-shadow: 0 10px 30px rgba(0,0,0,.18);
    font-family: "Lato", sans-serif;
  }
  .flyer-art { position: absolute; inset: 0; }
  .headline {
    position: absolute; left: 0; right: 0; top: 484px;
    text-align: center; white-space: nowrap;
    font-family: "Anton", sans-serif; font-weight: 400;
    font-size: 25px; line-height: 1; letter-spacing: .3px;
    color: var(--ink);
  }
  .speaker-name {
    position: absolute; left: 0; right: 0; top: 514px;
    text-align: center; white-space: nowrap;
    font-family: "Anton", sans-serif; font-weight: 400;
    font-size: 92px; line-height: 1; letter-spacing: 1px;
    background: linear-gradient(180deg, var(--blue-deep) 0%, var(--blue-strong) 55%, var(--blue-soft) 100%);
    -webkit-background-clip: text; background-clip: text;
    color: transparent;
  }
  .session-blurb {
    position: absolute; left: 40px; right: 40px; top: 622px;
    text-align: center;
    font-size: 17px; line-height: 1.3;
    color: var(--body-ink);
  }
  .invite {
    position: absolute; left: 0; right: 0; top: 756px;
    text-align: center;
  }
  .invite-line {
    font-family: "Lato", sans-serif; font-weight: 700;
    font-size: 23px; line-height: 1.15; color: var(--ink);
  }
  .phones {
    margin-top: 16px;
    display: flex; justify-content: center; align-items: center; gap: 14px;
    font-family: "Archivo Black", sans-serif;
    font-size: 30px; color: var(--ink);
  }
  .phone { display: flex; align-items: center; gap: 10px; }
  .phone-icon { width: 26px; height: 26px; }
  .or-badge {
    width: 30px; height: 30px; border: 2px solid var(--ink); border-radius: 50%;
    font-family: "Lato", sans-serif; font-weight: 700; font-size: 11px;
    display: flex; align-items: center; justify-content: center;
  }
</style>
</head>
<body>
  <main class="flyer">
    <svg class="flyer-art" width="700" height="912" viewBox="0 0 700 912">
      <defs>
        <linearGradient id="portraitTone" x1="0" y1="0" x2="0" y2="1">
          <stop offset="0" stop-color="var(--photo-top)"/>
          <stop offset=".45" stop-color="var(--photo-mid)"/>
          <stop offset="1" stop-color="var(--photo-low)"/>
        </linearGradient>
        <linearGradient id="bandTone" x1="0" y1="0" x2="1" y2="0">
          <stop offset="0" stop-color="var(--blue-soft)"/>
          <stop offset=".4" stop-color="var(--blue-mist)"/>
          <stop offset="1" stop-color="var(--blue-soft)"/>
        </linearGradient>
        <linearGradient id="midTone" x1="0" y1="0" x2="0" y2="1">
          <stop offset="0" stop-color="#f4f5f6"/>
          <stop offset="1" stop-color="#ffffff"/>
        </linearGradient>
      </defs>
      <rect width="700" height="912" fill="url(#midTone)"/>
      <path class="portrait" role="img" aria-label="Portrait photo of the life coach seated in a blue patterned blouse"
            d="M0 0 H700 V418 Q420 448 220 466 Q90 476 0 472 Z" fill="url(#portraitTone)"/>
      <path d="M0 728 Q300 710 700 690" stroke="var(--line-dark)" stroke-width="6" fill="none"/>
      <path d="M0 731 Q300 713 700 693 V912 H0 Z" fill="url(#bandTone)"/>
      <rect y="900" width="700" height="12" fill="var(--line-dark)"/>
    </svg>

    <h2 class="headline">A HEART TO HEART CONVERSATION WITH LIFE COACH</h2>
    <h1 class="speaker-name">TALIA BROOKS</h1>
    <p class="session-blurb">Let Us Bloom is an interactive soul searching session that will help women<br>share their stories and be real about the things that matter most.</p>

    <section class="invite">
      <p class="invite-line">To invite Talia to your<br>women's group or gathering.</p>
      <div class="phones">
        <span class="phone">
          <svg class="phone-icon" viewBox="0 0 24 24"><circle cx="12" cy="12" r="11" fill="none" stroke="#fff" stroke-width="2"/><path d="M8 6.5l2 2.5-1.2 1.4a7 7 0 0 0 4.8 4.8L15 14l2.5 2-1.3 1.8C11 17.5 6.5 13 6.2 7.8Z" fill="#fff"/></svg>
          555-210-4836
        </span>
        <span class="or-badge">OR</span>
        <span class="phone">
          <svg class="phone-icon" viewBox="0 0 24 24"><circle cx="12" cy="12" r="11" fill="none" stroke="#fff" stroke-width="2"/><path d="M8 6.5l2 2.5-1.2 1.4a7 7 0 0 0 4.8 4.8L15 14l2.5 2-1.3 1.8C11 17.5 6.5 13 6.2 7.8Z" fill="#fff"/></svg>
          555-9321
        </span>
      </div>
    </section>
  </main>
</body>
</html>
```